First Aid Training business needs business card design

We would like a double sided business card designed for a first aid training business - Brindlewood First Aid. We provide first aid training and , WHS (work, health and safety) training.

The attached word document contains the key information we would like on each side of the business card.

Final design needs to be delivered in print ready format, along with the original file.

```html
<!DOCTYPE html>
<html lang="en">
<head>
<meta charset="utf-8">
<title>Brindlewood First Aid – Business Card</title>
<link rel="stylesheet" href="https://fonts.googleapis.com/css2?family=Montserrat:wght@500;600;700;800&display=swap">
<style>
  :root {
    --bg: #f6b2b2;
    --red: #d44a4c;
    --red-deep: #cf3b3e;
    --black: #2b2b2b;
    --white: #ffffff;
    --paper: #f6f6f6;
    --tint: rgba(255,255,255,0.82);
  }
  * { box-sizing: border-box; margin: 0; padding: 0; }
  html, body { width: 1200px; height: 800px; overflow: hidden; }
  body {
    background: var(--bg);
    font-family: "Montserrat", sans-serif;
    display: flex;
    align-items: center;
    justify-content: center;
    gap: 40px;
  }
  .card {
    position: relative;
    width: 540px;
    height: 309px;
    overflow: hidden;
    box-shadow: 0 14px 30px rgba(120, 40, 40, 0.25);
  }

  /* Back side: services */
  .card-back { background: var(--paper); }
  .card-back .brand-panel {
    position: absolute; left: 0; top: 0; bottom: 0; width: 205px;
    background: var(--red-deep);
    display: flex; align-items: center; justify-content: center;
  }
  .brand-panel .mark-circle {
    width: 120px; height: 120px; border-radius: 50%;
    background: var(--tint);
  }
  .services {
    position: absolute; left: 230px; top: 34px; right: 18px;
    list-style: none;
    color: var(--red);
    font-size: 12.5px;
    font-weight: 600;
    line-height: 1.45;
  }
  .services li { position: relative; padding-left: 14px; }
  .services .lead { text-transform: uppercase; font-weight: 700; letter-spacing: 0.04em; }
  .services .sub { padding-left: 28px; }
  .services li::before {
    content: "•"; position: absolute; left: 0; top: 0;
  }
  .services .sub::before { content: "+"; left: 14px; font-weight: 800; }
  .services .gap { margin-top: 6px; }
  .web-band {
    position: absolute; left: 205px; right: 0; bottom: 0; height: 52px;
    background: var(--black);
    display: flex; align-items: center; justify-content: flex-end;
    gap: 12px; padding-right: 22px;
    color: var(--red);
    font-size: 13px; font-weight: 600; letter-spacing: 0.03em;
  }

  /* Front side: contact */
  .card-front { background: var(--red); }
  .card-front .logo-panel {
    position: absolute; left: 0; top: 0; bottom: 0; width: 235px;
    background: var(--white);
    border-top: 44px solid var(--black);
    border-bottom: 44px solid var(--black);
    display: flex; align-items: center; justify-content: center; gap: 8px;
  }
  .brand-dot { width: 20px; height: 20px; border-radius: 50%; background: var(--red); flex: none; }
  .brand-name {
    color: var(--black);
    font-weight: 800; font-size: 15px; line-height: 1.2;
    text-transform: uppercase; letter-spacing: 0.02em;
  }
  .contact {
    position: absolute; left: 235px; right: 0; top: 0; bottom: 0;
    padding: 58px 24px 0 20px;
    color: var(--white);
    text-align: right;
  }
  .person-name {
    font-size: 25px; font-weight: 800; letter-spacing: 0.08em;
    text-transform: uppercase; margin-bottom: 22px;
  }
  .contact-line {
    display: flex; align-items: center; justify-content: flex-end;
    gap: 10px; font-size: 12px; font-weight: 500; margin-bottom: 12px;
  }
  .icon { width: 22px; height: 22px; flex: none; }
</style>
</head>
<body>

  <section class="card card-back" aria-label="Card back">
    <div class="brand-panel"><div class="mark-circle"></div></div>
    <ul class="services">
      <li class="lead">We offer onsite training and can come to you</li>
      <li class="sub">Time efficient</li>
      <li class="sub">Cost effective</li>
      <li class="sub">Minimise downtime for your team</li>
      <li class="gap">First Aid Training</li>
      <li>WHS Training</li>
    </ul>
    <div class="web-band">
      <span>brindlewoodfirstaid.com.au</span>
      <svg class="icon" viewBox="0 0 22 22" aria-hidden="true">
        <circle cx="11" cy="11" r="11" fill="var(--red)"/>
        <g fill="none" stroke="var(--white)" stroke-width="1.2">
          <circle cx="11" cy="11" r="5.5"/>
          <ellipse cx="11" cy="11" rx="2.4" ry="5.5"/>
          <line x1="5.5" y1="11" x2="16.5" y2="11"/>
        </g>
      </svg>
    </div>
  </section>

  <section class="card card-front" aria-label="Card front">
    <div class="logo-panel">
      <span class="brand-dot"></span>
      <span class="brand-name">Brindlewood<br>First Aid Training</span>
    </div>
    <div class="contact">
      <h1 class="person-name">Daniel Harper</h1>
      <p class="contact-line">
        <span>0491 570 264</span>
        <svg class="icon" viewBox="0 0 22 22" aria-hidden="true">
          <circle cx="11" cy="11" r="11" fill="var(--white)"/>
          <path d="M8 6.5l1.6 0 .9 2.4-1.1.9a6 6 0 0 0 2.8 2.8l.9-1.1 2.4.9 0 1.6a1.2 1.2 0 0 1-1.3 1.2A8 8 0 0 1 6.8 7.8 1.2 1.2 0 0 1 8 6.5z" fill="var(--red)"/>
        </svg>
      </p>
      <p class="contact-line">
        <span>help@brindlewoodfirstaid.com.au</span>
        <svg class="icon" viewBox="0 0 22 22" aria-hidden="true">
          <circle cx="11" cy="11" r="11" fill="var(--white)"/>
          <g fill="none" stroke="var(--red)" stroke-width="1.2">
            <circle cx="11" cy="11" r="5.5"/>
            <ellipse cx="11" cy="11" rx="2.4" ry="5.5"/>
            <line x1="5.5" y1="11" x2="16.5" y2="11"/>
          </g>
        </svg>
      </p>
    </div>
  </section>

</body>
</html>
```